Velmorix E-commerce Website Design

I'm looking into having my e-comm website built. We are an investment company that is investing in a private label focused on a rising sport category called Pickleball in EU market.

We will provide top quality material and acessories for players be ready to go to courts. We will have a range of: Rackets, Set of balls, Net, Lines, overgrip, water bottle, player bag.

As it´s a new sports category we would like to see an architecture that alows us to share some storytelling about the category, the brand and lead to purchase of our products.

We will position our self as an inclusive and fun brand that you can reach out to find more info about Pickleball Sport, buy your pickleball stuff and have fun. Its all about action and fun.

Target Market(s)

Europe Market

Industry/Entity Type

Pickleball (Sports)

Coding

Coded - Design and coding required

Number of Pages Required

1 page

Requirements
Must have
• E-commerce look and feel
Nice to have
• A bit of storytelling about the brand and specially the category (Pickleball).

```html
<!DOCTYPE html>
<html lang="en">
<head>
<meta charset="utf-8">
<title>Velmorix – Pickleball Gear</title>
<link rel="stylesheet" href="https://fonts.googleapis.com/css2?family=Bebas+Neue&family=Poppins:wght@400;500;600;700&display=swap">
<style>
:root{
  --teal:#16768d;
  --teal-dark:#0e5366;
  --red:#e3173e;
  --pink:#d9005f;
  --ink:#1e1e1e;
  --grey-band:#e2e2e2;
  --grey-text:#8f8f8f;
  --dark:#2a2a2a;
  --white:#ffffff;
}
*{margin:0;padding:0;box-sizing:border-box}
html,body{width:1200px;height:4099px;overflow:hidden}
body{position:relative;background:var(--white);font-family:"Poppins",sans-serif;color:var(--ink)}
.abs{position:absolute}
.display{font-family:"Bebas Neue",sans-serif;font-weight:400}
.ghost{font-family:"Bebas Neue",sans-serif;color:transparent;-webkit-text-stroke:1.5px rgba(255,255,255,.13);letter-spacing:6px;white-space:nowrap}
.btn{position:absolute;display:flex;align-items:center;justify-content:center;background:var(--red);color:var(--white);font-size:12px;font-weight:600;letter-spacing:4px;clip-path:polygon(0 0,92% 0,100% 50%,92% 100%,0 100%)}
.circle-arrow{position:absolute;width:46px;height:46px;border-radius:50%;background:var(--pink);display:flex;align-items:center;justify-content:center}
.photo{position:absolute}

/* hero */
.hero{left:0;top:0;width:1200px;height:750px;background:linear-gradient(180deg,#1a7f97 0%,#136a80 100%);overflow:hidden}
.brand{left:125px;top:32px;font-size:50px;color:var(--white);letter-spacing:2px}
.nav{left:387px;top:50px;display:flex;gap:46px;font-size:11px;font-weight:600;letter-spacing:1.4px;color:var(--white)}
.nav .active{color:var(--white);border-bottom:2px solid var(--red);padding-bottom:4px}
.hero-title{left:125px;top:262px;font-size:58px;line-height:62px;color:var(--white);letter-spacing:.5px}
.hero-title .outline{color:transparent;-webkit-text-stroke:1.3px var(--white);border-bottom:3px solid var(--red)}
.hero-copy{left:125px;top:422px;width:510px;font-size:12.5px;line-height:22px;color:var(--white)}
.hero-tag{left:745px;top:684px;font-size:15px;color:var(--white);letter-spacing:.6px;display:flex;align-items:center;gap:14px}
.hero-tag::before{content:"";width:78px;height:1px;background:rgba(255,255,255,.8)}
.social-rail{left:33px;top:550px;display:flex;flex-direction:column;gap:22px}
.social-rail span{width:22px;height:22px;border-radius:50%;border:2px solid rgba(255,255,255,.45)}
.dots{left:1145px;top:326px;display:flex;flex-direction:column;gap:14px}
.dots span{width:8px;height:8px;border-radius:50%;background:rgba(255,255,255,.35)}
.dots span:first-child{width:12px;height:12px;margin-left:-2px;background:var(--white)}

/* category band */
.band{left:0;top:750px;width:1200px;height:120px;background:linear-gradient(90deg,#e3173e,#d9005f);display:flex;align-items:center;justify-content:space-between;padding:0 14px;color:var(--white)}
.band .word{font-family:"Bebas Neue",sans-serif;font-size:54px;letter-spacing:1px}
.band .word.thin{color:transparent;-webkit-text-stroke:1.4px var(--white)}
.band .dot{width:10px;height:10px;border-radius:50%;border:2px solid var(--white)}

/* products */
.stripes span{display:block;height:4px;background:var(--red);margin-bottom:7px}
.slider{left:125px;top:972px;width:950px;height:358px;display:flex}
.slide{flex:1;position:relative;display:flex;align-items:center;justify-content:center;text-align:center;color:var(--white);font-size:50px;line-height:48px}
.slide + .slide{border-left:2px solid var(--pink)}
.vert-brand{left:1080px;top:972px;width:70px;height:358px;display:flex;align-items:center;justify-content:center}
.vert-brand span{transform:rotate(90deg);font-family:"Bebas Neue",sans-serif;font-size:92px;color:#a7a7a7;letter-spacing:4px;white-space:nowrap}
.section-title{font-size:50px;color:var(--ink);letter-spacing:.5px}
.body-copy{font-size:12.5px;line-height:22px;color:#3a3a3a}

/* partners */
.partners{left:0;top:1562px;width:1200px;height:176px;background:var(--grey-band);display:flex;align-items:center;justify-content:space-between;padding:0 60px}
.partners span{font-size:26px;font-weight:600;color:var(--grey-text)}

/* news */
.news-panel{left:343px;top:2538px;width:857px;height:862px;background:linear-gradient(180deg,#16768d,#0f5a6d)}
.card{position:absolute;top:2783px;width:337px}
.card .photo{position:relative;width:337px;height:292px}
.card h3{font-family:"Bebas Neue",sans-serif;font-weight:400;font-size:24px;line-height:27px;margin-top:50px;letter-spacing:.4px}
.card p{font-size:12.5px;line-height:22px;margin-top:16px}
.card .more{display:flex;align-items:center;gap:16px;margin-top:26px;font-size:12.5px;font-weight:700;color:var(--red)}
.card .more::after{content:"";width:38px;height:1px;background:var(--red)}
.card.light{color:var(--white)}
.card.dark{color:var(--ink)}

/* footer */
.footer-mark{left:0;top:3505px;width:1200px;display:flex;justify-content:center;align-items:center;gap:18px}
.footer-mark i{width:54px;height:54px;background:var(--pink)}
.footer-mark span{font-family:"Bebas Neue",sans-serif;font-size:96px;color:var(--pink);letter-spacing:4px;line-height:1}
.footer-nav{left:125px;top:3767px;width:950px;height:71px;background:var(--red);display:flex;justify-content:center;align-items:center;gap:72px;font-size:13px;font-weight:600;letter-spacing:1.6px;color:var(--white)}
.footer-social{left:0;top:3889px;width:1200px;display:flex;justify-content:center;gap:25px}
.footer-social span{width:46px;height:46px;border-radius:50%}
.copyright{left:0;top:4037px;width:1200px;height:62px;background:var(--dark);color:var(--white);font-size:13px;display:flex;align-items:center;justify-content:center}
</style>
</head>
<body>

<!-- HERO -->
<section class="abs hero">
  <div class="abs ghost" style="left:120px;top:105px;font-size:88px">RACKETS</div>
  <div class="abs ghost" style="left:620px;top:105px;font-size:88px">OVER GRIP</div>
  <div class="abs ghost" style="left:515px;top:185px;font-size:88px">NET</div>
  <div class="abs ghost" style="left:290px;top:565px;font-size:88px">WATER BOTTLE</div>
  <div class="abs ghost" style="left:125px;top:648px;font-size:88px">LINES</div>
  <div class="abs ghost" style="left:-40px;top:260px;font-size:70px;transform:rotate(90deg);transform-origin:left top;left:80px;top:30px">PLAYER BAG</div>
  <div class="abs ghost" style="font-size:70px;transform:rotate(90deg);transform-origin:left top;left:1145px;top:220px">SETS OF BALL</div>

  <div class="photo" role="img" aria-label="Pickleball player in white t-shirt and shorts lunging with a paddle" style="left:460px;top:80px;width:660px;height:670px;background:radial-gradient(ellipse at 55% 45%,rgba(230,230,230,.55) 0%,rgba(200,190,180,.35) 35%,rgba(22,118,141,0) 70%)"></div>

  <div class="abs brand display">VELMORIX</div>
  <nav class="abs nav"><span class="active">HOME</span><span>ABOUT US</span><span>OUR PRODUCTS</span><span>CONTACT US</span></nav>
  <svg class="abs" style="left:1001px;top:47px" width="22" height="22" viewBox="0 0 22 22" fill="none" stroke="#fff" stroke-width="2"><circle cx="9" cy="9" r="7"/><path d="M14 14l6 6"/></svg>
  <svg class="abs" style="left:1046px;top:42px" width="28" height="26" viewBox="0 0 28 26" fill="none" stroke="#fff" stroke-width="2"><path d="M3 10h22l-3 12H6z"/><path d="M9 10l5-7 5 7"/><circle cx="24" cy="4" r="3" fill="#e3173e" stroke="none"/></svg>
  <div class="abs" style="left:1120px;top:132px;width:80px">
    <div style="height:4px;background:var(--red);margin-bottom:8px"></div>
    <div style="height:4px;background:var(--red);margin-left:18px"></div>
  </div>

  <h1 class="abs hero-title display">Buy Your <span class="outline">PICKLEBALL</span><br>Stuff And Have Fun</h1>
  <p class="abs hero-copy">Lorem Ipsum is simply dummy text of the printing and typesetting industry. Lorem Ipsum has been the industry's standard dummy text ever since the 1500s,</p>
  <a class="btn" style="left:125px;top:518px;width:167px;height:38px">SHOP NOW</a>

  <div class="abs social-rail" aria-label="Social links"><span></span><span></span><span></span><span></span></div>
  <div class="abs dots"><span></span><span></span><span></span><span></span><span></span></div>
  <div class="abs hero-tag">Its all about action and fun.</div>
</section>

<!-- CATEGORY BAND -->
<div class="abs band">
  <span class="word thin">RACKETS</span><span class="dot"></span>
  <span class="word">LINES</span><span class="dot"></span>
  <span class="word thin">NET</span><span class="dot"></span>
  <span class="word">WATER BOTTLE</span><span class="dot"></span>
  <span class="word thin">OVER GRIP</span>
</div>

<!-- PRODUCTS -->
<div class="abs stripes" style="left:52px;top:1003px;width:73px"><span></span><span style="margin-left:10px"></span><span></span></div>
<div class="abs slider">
  <div class="slide display" role="img" aria-label="Colourful pickleball paddles arranged in a circle" style="background:radial-gradient(circle at 50% 50%,#1a2c3a,#23413d 60%,#3a3050)">RACKETS</div>
  <div class="slide display" role="img" aria-label="Pickleball net on a green court" style="background:linear-gradient(180deg,#1b1b1b,#2e3b22 60%,#3d5a26)">NET</div>
  <div class="slide display" role="img" aria-label="Dark water bottle" style="background:linear-gradient(180deg,#0e0e0e,#2c2c2c)">WATER<br>BOTTLE</div>
</div>
<div class="circle-arrow" style="left:102px;top:1127px"><svg width="12" height="12" viewBox="0 0 12 12" fill="none" stroke="#fff" stroke-width="2"><path d="M8 2L4 6l4 4"/></svg></div>
<div class="circle-arrow" style="left:1052px;top:1127px"><svg width="12" height="12" viewBox="0 0 12 12" fill="none" stroke="#fff" stroke-width="2"><path d="M4 2l4 4-4 4"/></svg></div>
<div class="abs vert-brand"><span>VELMORIX</span></div>

<h2 class="abs section-title display" style="left:125px;top:1362px">OUR PRODUCTS</h2>
<p class="abs body-copy" style="left:125px;top:1424px;width:450px">Lorem Ipsum is simply dummy text of the printing and typesetting industry. Lorem Ipsum has been the industry's standard</p>
<a class="btn" style="left:908px;top:1392px;width:167px;height:41px">VIEW ALL</a>

<!-- PARTNERS -->
<div class="abs partners">
  <span>Brightfund</span><span>Chirpline</span><span>Carton</span><span>Pinmark</span><span>Rydo</span><span>Storely</span><span>Tablery</span><span>Huddlo</span>
</div>

<!-- ABOUT -->
<h2 class="abs section-title display" style="left:125px;top:1860px">ABOUT US</h2>
<div class="abs body-copy" style="left:125px;top:1935px;width:425px">
  <p>Lorem Ipsum is simply dummy text of the printing and typesetting industry. Lorem Ipsum has been the industry's standard dummy text ever since the 1500s, when an unknown printer took a galley of type and scrambled it to make a type specimen book. It has survived not only five centuries, but also the leap into electronic typesetting, remaining essentially unchanged. It was popularised in the 1960s with the release of Letraset sheets containing Lorem Ipsum passages, and more recently with desktop publishing software like Aldus PageMaker including versions of Lorem Ipsum.</p>
  <p style="margin-top:12px">Lorem Ipsum is simply dummy text of the printing and typesetting industry. Lorem Ipsum has been the industry's standard dummy text</p>
</div>
<a class="btn" style="left:125px;top:2262px;width:182px;height:40px">READ MORE</a>

<div class="abs" style="left:670px;top:1838px;width:405px;height:537px;background:var(--white);box-shadow:0 6px 26px rgba(0,0,0,.15)"></div>
<div class="abs" style="left:693px;top:1870px;width:360px;height:475px;background:var(--red)"></div>
<div class="photo" role="img" aria-label="Woman in pink shirt and sunglasses playing pickleball" style="left:717px;top:1893px;width:313px;height:429px;background:linear-gradient(180deg,#f2f2f2,#e8e4e6 55%,#d9d3d6)"></div>
<div class="abs" style="left:528px;top:2228px;width:317px;height:210px;background:var(--teal)"></div>
<div class="photo" role="img" aria-label="Three smiling pickleball players on a blue court" style="left:552px;top:2167px;width:370px;height:246px;background:linear-gradient(135deg,#7ba9c9,#4d7fa8 50%,#c98aa8)"></div>
<div class="abs stripes" style="left:1085px;top:2307px;width:88px"><span></span><span style="margin-left:12px"></span><span></span></div>

<!-- NEWS -->
<div class="abs news-panel"></div>
<h2 class="abs section-title display" style="right:125px;top:2628px;color:var(--white)">NEWS &amp; BLOGS</h2>
<p class="abs body-copy" style="right:125px;top:2694px;width:570px;text-align:right;color:var(--white)">Lorem Ipsum is simply dummy text of the printing and typesetting industry. Lorem Ipsum has been the industry's standard</p>

<article class="card dark" style="left:18px">
  <div class="photo" role="img" aria-label="Players on an outdoor teal pickleball court with palm trees" style="background:linear-gradient(180deg,#bcd6e6 0%,#8fb08a 40%,#2aa0a8 75%,#1b7f8a)"></div>
  <h3>Lorem Ipsum Is Simply Dummy Text Of The Printing</h3>
  <p>Lorem Ipsum is simply dummy text of the printing and typesetting industry. Lorem Ipsum has been the industry's standard</p>
  <div class="more">Read more</div>
</article>
<article class="card light" style="left:377px">
  <div class="photo" role="img" aria-label="Player hitting a ball at a professional pickleball event" style="background:linear-gradient(180deg,#1f4fb0 0%,#2a5fc4 50%,#b0503c 80%,#9a4132)"></div>
  <h3>Lorem Ipsum Is Simply Dummy Text Of The Printing</h3>
  <p>Lorem Ipsum is simply dummy text of the printing and typesetting industry. Lorem Ipsum has been the industry's standard</p>
  <div class="more">Read more</div>
</article>
<article class="card light" style="left:737px">
  <div class="photo" role="img" aria-label="Two smiling women holding pickleball paddles" style="background:linear-gradient(180deg,#5a5a5a 0%,#8a7d70 45%,#e9e6e3 85%)"></div>
  <h3>Lorem Ipsum Is Simply Dummy Text Of The Printing</h3>
  <p>Lorem Ipsum is simply dummy text of the printing and typesetting industry. Lorem Ipsum has been the industry's standard</p>
  <div class="more">Read more</div>
</article>
<div class="circle-arrow" style="left:1054px;top:2883px;width:40px;height:40px"><svg width="10" height="10" viewBox="0 0 12 12" fill="none" stroke="#fff" stroke-width="2"><path d="M8 2L4 6l4 4"/></svg></div>
<div class="circle-arrow" style="left:1054px;top:2937px;width:40px;height:40px"><svg width="10" height="10" viewBox="0 0 12 12" fill="none" stroke="#fff" stroke-width="2"><path d="M4 2l4 4-4 4"/></svg></div>

<!-- FOOTER -->
<div class="abs footer-mark"><i></i><span>VELMORIX</span></div>
<p class="abs body-copy" style="left:300px;top:3683px;width:600px;text-align:center">Lorem Ipsum is simply dummy text of the printing and typesetting industry. Lorem Ipsum has been the industry's standard dummy text ever since the 1500s,</p>
<nav class="abs footer-nav"><span>HOME</span><span>ABOUT US</span><span>OUR PRODUCTS</span><span>CONTACT US</span></nav>
<div class="abs footer-social" aria-label="Social links">
  <span style="background:#1877f2"></span><span style="background:#1d9bf0"></span><span style="background:#d62f8a"></span><span style="background:#0a66c2"></span>
</div>
<div class="abs copyright">Copyright@2023-Velmorix-Privacy Policy</div>

</body>
</html>
```